Lantern Motion for Neighbors Business Cards

I need business cards for staff in a new startup. Our company name is Movrela - we train Tai Chi teachers. But our biggest project is called Lantern Motion for Neighbors - a federal project to put together free Tai Chi classes for Vets all across America. It's a young company, with a spirit of excitement, passion, a desire to do good for others (our Vets) and a modern style and sensibility. In other words, not old-fashioned Asian martial arts theme, but something new.

Industry/Entity Type

Health And Wellness

Contact Information for Business Card

The topic is ancient healing, but the company is the Pembrooks - so I'd like a card design that captures that.

Font styles to use
Sans Serif

Colors

Designer to choose colors to be used in the design.

Requirements
Nice to have
• I've got two logos - one for the company and one for the project. I want to see if we can incorporate them both without it becoming too busy.
Should not have
• Overly old-fashioned yin-yang themes.

```html
<!DOCTYPE html>
<html lang="en">
<head>
<meta charset="utf-8">
<title>Lantern Motion for Neighbors Business Cards</title>
<link rel="stylesheet" href="https://fonts.googleapis.com/css2?family=Roboto:wght@400;500;700&display=swap">
<style>
  :root {
    --backdrop: #2b2c2e;
    --card-dark: #1d1e20;
    --card-white: #ffffff;
    --navy: #2e2d72;
    --red: #e0101e;
    --gold: #f2d774;
    --ink-light: #ffffff;
  }
  html, body {
    margin: 0;
    padding: 0;
    width: 1200px;
    height: 960px;
    overflow: hidden;
    background: var(--backdrop);
    font-family: "Roboto", sans-serif;
  }
  .canvas {
    position: relative;
    width: 1200px;
    height: 960px;
  }
  .card {
    position: absolute;
    width: 560px;
    height: 320px;
    overflow: hidden;
    box-shadow: 0 14px 30px rgba(0,0,0,0.45);
  }
  /* Back of card */
  .card-back {
    left: 70px;
    top: 90px;
    background: var(--card-dark);
  }
  .company-mark {
    position: absolute;
    left: 50%;
    top: 50%;
    transform: translate(-50%, -50%);
    display: flex;
    align-items: center;
    gap: 16px;
  }
  .company-mark .dot {
    width: 72px;
    height: 72px;
    border-radius: 50%;
    background: var(--red);
  }
  .company-mark .name {
    font-size: 44px;
    font-weight: 700;
    color: var(--gold);
    letter-spacing: 1px;
  }
  /* Front of card */
  .card-front {
    left: 570px;
    top: 560px;
    background: var(--card-white);
  }
  .card-front .wave {
    position: absolute;
    inset: 0;
  }
  .project-mark {
    position: absolute;
    left: 238px;
    top: 52px;
    display: flex;
    align-items: center;
    gap: 12px;
  }
  .project-mark .ring {
    width: 50px;
    height: 50px;
    border-radius: 50%;
    border: 3px solid var(--navy);
    box-sizing: border-box;
  }
  .project-mark .name {
    font-size: 19px;
    font-weight: 500;
    color: var(--navy);
    line-height: 1.15;
    text-transform: uppercase;
    letter-spacing: 0.5px;
  }
  .person {
    position: absolute;
    left: 40px;
    bottom: 16px;
    color: var(--ink-light);
  }
  .person .full-name {
    font-size: 22px;
    font-weight: 700;
    margin: 0;
  }
  .person .role {
    font-size: 14px;
    font-weight: 500;
    margin: 2px 0 10px;
  }
  .person .address {
    font-size: 13px;
    line-height: 1.35;
    margin: 0;
  }
  .contact {
    position: absolute;
    right: 22px;
    top: 206px;
    list-style: none;
    margin: 0;
    padding: 0;
    color: var(--ink-light);
    font-size: 13px;
    text-align: right;
  }
  .contact li {
    display: flex;
    justify-content: flex-end;
    align-items: center;
    gap: 7px;
    margin-bottom: 4px;
  }
  .contact svg {
    width: 11px;
    height: 11px;
    fill: var(--ink-light);
  }
</style>
</head>
<body>
<div class="canvas">

  <section class="card card-back" aria-label="Card back">
    <div class="company-mark">
      <span class="dot"></span>
      <span class="name">Movrela</span>
    </div>
  </section>

  <section class="card card-front" aria-label="Card front">
    <svg class="wave" viewBox="0 0 560 320" width="560" height="320" aria-hidden="true">
      <path d="M0 230 C40 200 110 192 200 188 C320 182 420 172 470 140 C515 110 532 60 518 0 L560 0 L560 320 L0 320 Z" fill="var(--navy)"/>
      <path d="M0 214 C40 184 110 176 200 172 C320 166 410 156 456 126 C498 98 514 55 504 0" fill="none" stroke="var(--red)" stroke-width="5"/>
    </svg>

    <div class="project-mark">
      <span class="ring"></span>
      <span class="name">Lantern Motion<br>for Neighbors</span>
    </div>

    <div class="person">
      <p class="full-name">Daniel Hartwell</p>
      <p class="role">President</p>
      <p class="address">4120 Birchwood Road<br>Juneau, Alaska 99801</p>
    </div>

    <ul class="contact">
      <li>555-201-4836
        <svg viewBox="0 0 24 24"><path d="M6.6 10.8a15 15 0 0 0 6.6 6.6l2.2-2.2a1 1 0 0 1 1-.25 11.4 11.4 0 0 0 3.6.57 1 1 0 0 1 1 1V20a1 1 0 0 1-1 1A17 17 0 0 1 3 4a1 1 0 0 1 1-1h3.5a1 1 0 0 1 1 1c0 1.25.2 2.45.57 3.57a1 1 0 0 1-.25 1z"/></svg>
      </li>
      <li>555-307-9124
        <svg viewBox="0 0 24 24"><path d="M7 1h10a2 2 0 0 1 2 2v18a2 2 0 0 1-2 2H7a2 2 0 0 1-2-2V3a2 2 0 0 1 2-2zm0 3v14h10V4z"/></svg>
      </li>
      <li>info@lanternmotion.org
        <svg viewBox="0 0 24 24"><path d="M2 5h20v14H2zm2 2v.5l8 5 8-5V7z"/></svg>
      </li>
      <li>www.lanternmotion.org
        <svg viewBox="0 0 24 24"><circle cx="12" cy="12" r="10"/></svg>
      </li>
    </ul>
  </section>

</div>
</body>
</html>
```